Ongoing work and Exhibition stand design for Harbour Panels

I need a simple layout/sketch for a 3 x 3m stand for a trade show (see examples of stand designs below). It is a corner stand so will only have 2 walls for display. There will be a TV on one wall. One island bench or table will be needed to write on and display flyers.

The stand is a shell scheme which means it has a floor, lights and an aluminium frame already supplied.

We sell kitchen doors (and wardrobe doors). I need to show sample doors 300 x 400mm but can make them in any size to suit. I want a simple but original way of showing the doors and I want the stand to be noticed!

Headline graphics to include the text "Renovating your kitchen? Just replace the doors, saving you thousands of $$$. Improve the value of your home at a fraction of the cost." Graphics to include kitchen picture(s) attached.

The main colour scheme would be the orange of our brochure (see brochure attached).

Ongoing work will probably be offered to the winner of this project.

Needed ASAP! Thanks.

Target Market(s)

The do it yourself DIY home renovator. Male and female home owners age group 25-55.

Industry/Entity Type

Trade

Requirements
Must have
• Clean and simple but eye catching design.

```html
<!DOCTYPE html>
<html lang="en">
<head>
<meta charset="utf-8">
<title>Harbour Panels – Exhibition Stand Walls</title>
<link rel="stylesheet" href="https://fonts.googleapis.com/css2?family=Archivo+Black&family=Arimo:ital,wght@0,400;0,700;1,400;1,700&display=swap">
<style>
  :root{
    --backdrop:#6c6c6c;
    --orange:#f39a1e;
    --orange-light:#f7b04a;
    --ink:#141414;
    --white:#ffffff;
    --frame:#b9bcc0;
    --kitchen-warm:#c9b8a2;
    --kitchen-floor:#9a3e1c;
    --screen:#1b1b1b;
    --door-pale:#e4ebe9;
    --door-blue:#cfe2f0;
    --door-panel:#eef3f7;
  }
  *{box-sizing:border-box;margin:0;padding:0}
  html,body{width:1200px;height:900px;overflow:hidden}
  body{background:var(--backdrop);font-family:"Arimo",Arial,sans-serif;position:relative}

  .stand-walls{position:absolute;left:50px;top:150px;width:1100px;height:600px;display:flex;gap:10px}
  .wall{position:relative;height:600px;border:6px solid var(--frame);overflow:hidden}

  /* left wall */
  .wall--kitchen{width:520px}
  .kitchen-photo{position:absolute;inset:0;background:linear-gradient(180deg,#f4f1ec 0%,var(--kitchen-warm) 45%,#e9e6e0 62%,var(--kitchen-floor) 100%)}
  .headline-banner{position:absolute;left:0;top:188px;width:380px;height:110px;background:var(--orange);
    display:flex;flex-direction:column;justify-content:center;padding-left:30px}
  .headline-banner span{font-family:"Archivo Black",Arial,sans-serif;color:var(--ink);font-size:34px;line-height:1.1;letter-spacing:5px}
  .headline-banner span + span{letter-spacing:1px}
  .tv-screen{position:absolute;left:396px;top:192px;width:100px;height:76px;background:var(--screen);border:3px solid #444;
    color:var(--white);font-size:10px;font-weight:700;text-align:center;display:flex;align-items:center;justify-content:center;line-height:1.3}
  .brand-strip{position:absolute;left:18px;bottom:24px;display:flex;align-items:center;gap:10px}
  .brand-mark{width:34px;height:34px;background:var(--orange-light)}
  .brand-text{color:var(--white);font-size:11px;line-height:1.35}
  .brand-text .brand-name{font-size:14px;font-weight:700}
  .brand-text em{font-weight:700}

  /* right wall */
  .wall--doors{width:570px;background:var(--orange)}
  .doors-headline{position:absolute;left:0;top:10px;width:100%;text-align:center}
  .doors-headline h1{font-family:"Archivo Black",Arial,sans-serif;font-size:29px;letter-spacing:1px;color:var(--ink);font-weight:400;white-space:nowrap;line-height:1.15}
  .doors-headline p{font-style:italic;color:var(--white);font-size:22px;line-height:1.2;margin-top:2px}
  .image-strip{position:absolute;left:0;top:100px;width:100%;height:128px;display:flex;gap:6px;padding:0 6px;background:#1e1e1e}
  .swatch-art{flex:1;background:linear-gradient(90deg,#8fb1b9,#d4c4a6,#7fa0b0)}
  .room-photo{flex:1.1;background:linear-gradient(180deg,#dfe3e6,#b9bdc0 70%,#6b5d52)}
  .swatch-art--right{background:linear-gradient(90deg,#a2b9d3,#c9a6c2,#d8c7a7)}

  .quote-badge{position:absolute;left:218px;top:206px;width:84px;height:84px;border-radius:50%;background:var(--orange);
    border:3px solid var(--white);color:var(--white);font-weight:700;font-size:14px;text-align:center;line-height:1.05;
    display:flex;align-items:center;justify-content:center;transform:rotate(-12deg)}
  .quote-badge b{font-size:17px;display:block}
  .feature{position:absolute;color:var(--white);font-size:12px;font-weight:700;text-align:center;line-height:1.25}
  .feature--delivery{left:56px;top:246px}
  .feature--install{left:312px;top:246px}
  .feature strong{font-size:13px}

  .wardrobe-callout{position:absolute;left:12px;top:290px;width:388px;color:var(--ink);text-align:center}
  .wardrobe-callout h2{font-family:"Arimo",Arial,sans-serif;font-weight:700;font-size:21px;white-space:nowrap}
  .wardrobe-callout p{font-size:11px;color:var(--white);line-height:1.3;margin-top:2px}

  .door-samples{position:absolute;left:12px;top:358px;width:386px;display:grid;grid-template-columns:repeat(5,1fr);gap:14px 10px}
  .door-sample{height:98px;background:var(--door-pale);border:2px solid var(--white)}
  .door-sample:nth-child(2n){background:var(--door-blue)}

  .actual-door-panel{position:absolute;right:0;top:228px;width:148px;height:366px;background:var(--white)}
  .actual-door{position:absolute;inset:8px;background:linear-gradient(180deg,var(--door-panel),#dfe7ee);
    display:flex;align-items:flex-start;justify-content:center;padding-top:80px}
  .actual-door span{font-weight:700;font-size:13px;text-align:center;color:var(--ink);line-height:1.2}
</style>
</head>
<body>
  <main class="stand-walls">
    <section class="wall wall--kitchen">
      <div class="kitchen-photo" role="img" aria-label="Photo of a white shaker-style kitchen with timber floor"></div>
      <div class="headline-banner"><span>RENOVATING</span><span>YOUR KITCHEN?</span></div>
      <div class="tv-screen">FLATSCREEN<br>MONITOR</div>
      <div class="brand-strip">
        <div class="brand-mark"></div>
        <div class="brand-text">
          <div class="brand-name">Harbour Panels</div>
          <em>Top Quality Fast Service</em><br>
          HARBOUR PANELS 12 Quay Lane, Harbourside<br>
          Ph 9000 1234 • Fx 9000 5678 • Email sales@harbourpanels.com.au
        </div>
      </div>
    </section>

    <section class="wall wall--doors">
      <header class="doors-headline">
        <h1>JUST REPLACE THE DOORS</h1>
        <p>Saving you thousands of $$$</p>
      </header>
      <div class="image-strip">
        <div class="swatch-art" role="img" aria-label="Angled stack of coloured door edge samples"></div>
        <div class="room-photo" role="img" aria-label="Photo of a bedroom with white wardrobe doors"></div>
        <div class="swatch-art swatch-art--right" role="img" aria-label="Angled stack of coloured door edge samples"></div>
      </div>
      <div class="feature feature--delivery"><strong>AUSTRALIA</strong><br>Wide Delivery</div>
      <div class="feature feature--install">DIY Measure<br>&amp; Install</div>
      <div class="quote-badge"><div>Get a<b>QUOTE</b>now!</div></div>
      <div class="wardrobe-callout">
        <h2>We do WARDROBE DOORS too!</h2>
        <p>Download a quote @ www.harbourpanels.com.au<br>Send your door sizes for quote today!</p>
      </div>
      <div class="door-samples">
        <div class="door-sample" role="img" aria-label="Sample door"></div>
        <div class="door-sample" role="img" aria-label="Sample door"></div>
        <div class="door-sample" role="img" aria-label="Sample door"></div>
        <div class="door-sample" role="img" aria-label="Sample door"></div>
        <div class="door-sample" role="img" aria-label="Sample door"></div>
        <div class="door-sample" role="img" aria-label="Sample door"></div>
        <div class="door-sample" role="img" aria-label="Sample door"></div>
        <div class="door-sample" role="img" aria-label="Sample door"></div>
        <div class="door-sample" role="img" aria-label="Sample door"></div>
        <div class="door-sample" role="img" aria-label="Sample door"></div>
      </div>
      <div class="actual-door-panel">
        <div class="actual-door" role="img" aria-label="Full size white arched panel door">
          <span>ACTUAL SIZE<br>DOOR</span>
        </div>
      </div>
    </section>
  </main>
</body>
</html>
```